Vitamin B12 Liquid Drops Label

hi, i need a label designed for my vitamin b12 drops that i am going to be selling on bazaroo. the label needs to quickly capture the attention of a buyer as he or she is scrolling through the thumbnail search results on bazaroo.example my brand is called zulpa. i already have an example brand logo i will be using, however, i need help designing the rest of the label. attached are some examples of labels i like for other supplements.some of these examples are pink. i do not want pink. please go for a blue/green color scheme. THE DESIGN MUST BE BOLD

Target Market(s)

adults ages 30 - 64

Font styles to use
Sans Serif

Colors
0455a3
cedeed
3176b5
85acd3
cfdeed
9bcb3b
abd037
cadf82
00a990

Requirements
Must have
• - bold design
• - somewhat gender-neutral color scheme because this will be used equally by men and women
• - B12 MUST be very prominent and visible on the label
Should not have
• - it should not be "crunchy" looking

```html
<!DOCTYPE html>
<html lang="en">
<head>
<meta charset="utf-8">
<title>Zulpa B12 Vitamin Drops Labels</title>
<link rel="stylesheet" href="https://fonts.googleapis.com/css2?family=Oswald:wght@400;500&family=Montserrat:wght@500;800&display=swap">
<style>
  :root {
    --page-bg: #f1f1f1;
    --label-white: #ffffff;
    --blue-deep: #0455a3;
    --blue-mid: #3176b5;
    --blue-soft: #85acd3;
    --blue-pale: #cedeed;
    --green-deep: #0a7560;
    --green-mid: #00a990;
    --green-soft: #5cbfa8;
    --lime-soft: #cadf82;
    --lime-mid: #abd037;
  }
  html, body {
    margin: 0;
    padding: 0;
    overflow: hidden;
  }
  body {
    width: 1200px;
    height: 1200px;
    background: var(--page-bg);
    position: relative;
  }
  .label {
    position: absolute;
    top: 300px;
    width: 450px;
    height: 600px;
    box-shadow: 0 10px 30px rgba(0,0,0,0.12);
  }
  .label--blue { left: 100px; }
  .label--green { left: 650px; }
  .label__hero {
    font-family: "Oswald", "Arial Narrow", sans-serif;
    font-weight: 500;
    font-size: 340px;
    fill: var(--label-white);
  }
  .label__title {
    font-family: "Oswald", "Arial Narrow", sans-serif;
    font-weight: 400;
    text-anchor: middle;
  }
  .label__byline {
    font-family: "Montserrat", Arial, sans-serif;
    font-weight: 500;
    font-size: 14px;
    text-anchor: middle;
    fill: #777777;
  }
  .label__brand {
    font-family: "Montserrat", Arial, sans-serif;
    font-weight: 800;
    font-size: 40px;
    letter-spacing: 2px;
    text-anchor: middle;
    fill: var(--label-white);
  }
  .label--blue .label__title { fill: var(--blue-deep); }
  .label--green .label__title { fill: var(--green-deep); }
</style>
</head>
<body>

<svg class="label label--blue" viewBox="0 0 450 600" aria-label="Zulpa B12 vitamin drops label, blue">
  <defs>
    <linearGradient id="heroBlue" x1="0" y1="0" x2="1" y2="0">
      <stop offset="0" stop-color="var(--blue-deep)"/>
      <stop offset="0.55" stop-color="var(--blue-mid)"/>
      <stop offset="1" stop-color="var(--blue-soft)"/>
    </linearGradient>
    <linearGradient id="facetBlue" x1="0" y1="0" x2="1" y2="1">
      <stop offset="0" stop-color="var(--blue-pale)" stop-opacity="0.2"/>
      <stop offset="1" stop-color="var(--blue-soft)" stop-opacity="0.7"/>
    </linearGradient>
  </defs>
  <rect class="label__base" width="450" height="600" fill="var(--label-white)"/>
  <rect role="img" aria-label="Angular faceted pattern in pale blue" x="260" y="270" width="190" height="330" fill="url(#facetBlue)"/>
  <path class="label__hero-band" d="M0 0 H450 V275 H310 C265 275 240 290 225 335 C210 290 185 275 140 275 H0 Z" fill="url(#heroBlue)"/>
  <text class="label__hero" x="10" y="272" textLength="432" lengthAdjust="spacingAndGlyphs">B12</text>
  <text class="label__title" x="225" y="418" font-size="50">VITAMIN</text>
  <text class="label__title" x="225" y="478" font-size="58">DROPS</text>
  <line x1="120" y1="515" x2="180" y2="515" stroke="#999" stroke-width="1"/>
  <text class="label__byline" x="225" y="520">product by</text>
  <line x1="270" y1="515" x2="330" y2="515" stroke="#999" stroke-width="1"/>
  <rect class="label__brand-box" x="110" y="548" width="230" height="52" fill="var(--blue-deep)"/>
  <text class="label__brand" x="225" y="589">ZULPA</text>
</svg>

<svg class="label label--green" viewBox="0 0 450 600" aria-label="Zulpa B12 vitamin drops label, green">
  <defs>
    <linearGradient id="heroGreen" x1="0" y1="0" x2="1" y2="0">
      <stop offset="0" stop-color="var(--green-deep)"/>
      <stop offset="0.55" stop-color="var(--green-mid)"/>
      <stop offset="1" stop-color="var(--green-soft)"/>
    </linearGradient>
    <linearGradient id="facetGreen" x1="0" y1="0" x2="1" y2="1">
      <stop offset="0" stop-color="var(--lime-soft)" stop-opacity="0.5"/>
      <stop offset="1" stop-color="var(--lime-mid)" stop-opacity="0.7"/>
    </linearGradient>
  </defs>
  <rect class="label__base" width="450" height="600" fill="var(--label-white)"/>
  <rect role="img" aria-label="Angular faceted pattern in lime and mint green" x="260" y="270" width="190" height="330" fill="url(#facetGreen)"/>
  <path class="label__hero-band" d="M0 0 H450 V275 H310 C265 275 240 290 225 335 C210 290 185 275 140 275 H0 Z" fill="url(#heroGreen)"/>
  <text class="label__hero" x="10" y="272" textLength="432" lengthAdjust="spacingAndGlyphs">B12</text>
  <text class="label__title" x="225" y="418" font-size="50">VITAMIN</text>
  <text class="label__title" x="225" y="478" font-size="58">DROPS</text>
  <line x1="120" y1="515" x2="180" y2="515" stroke="#999" stroke-width="1"/>
  <text class="label__byline" x="225" y="520">product by</text>
  <line x1="270" y1="515" x2="330" y2="515" stroke="#999" stroke-width="1"/>
  <rect class="label__brand-box" x="110" y="548" width="230" height="52" fill="var(--green-mid)"/>
  <text class="label__brand" x="225" y="589">ZULPA</text>
</svg>

</body>
</html>
```